Supplement Bottle Label Design and Creative Lifestyle Images

We are a medical home consumer brand and we are releasing a supplement line of products called "Velbrook Nutrition". We are in need of a supplement bottle design for our supplement line, Velbrook Nutrition. We are looking for a very appealing, simple, and clean design, but with a medical feel to it.

We would like to see designs with a black background as well as designs with a white background. Bottle size will approximately be 200cc and label will about be 7" x 2.5", but this size is subject to change.

We really like the Pirlen Nutrition design and the Gantry Lab, however, we like the medical style of Nutrition Keystones. Please reference the links below.

To start off, the title of this bottle will be "Calm-Spire". We will need all similar warning about FDA, made in USA, non-GMA, GMP, ect. Please use the formula below to start:

2 Pills per serving
Blueberry pterostilbene - 10mg
Bacopa - 150mg
Gingko Biloba - 50mg
Vinpocetine - 10mg
Alpha-GPC -150mg
TAU - 35mg

https://www.shopvarn.example/Pirlen-Nutrition/b/ref=bl_dp_s_web_48213907562?ie=UTF8&node=48213907562&field-lbr_brands_browse-bin=Pirlen+Nutrition

https://www.shopvarn.example/l/7394208156

https://www.shopvarn.example/Nutrition-Keystones/b/ref=bl_dp_s_web_86420531977?ie=UTF8&node=86420531977&field-lbr_brands_browse-bin=Nutrition+Keystones

Industry/Entity Type

Medical

```html
<!DOCTYPE html>
<html lang="en">
<head>
<meta charset="UTF-8">
<title>Velbrook Nutrition – Supplement Label</title>
<link href="https://fonts.googleapis.com/css2?family=Montserrat:wght@500;600;700&family=Questrial&display=swap" rel="stylesheet">
<style>
  :root {
    --backdrop: #c0c0c0;
    --label-black: #000000;
    --ink-white: #ffffff;
    --accent-blue: #00a8e8;
    --font-display: "Montserrat", sans-serif;
    --font-body: "Questrial", sans-serif;
  }
  html, body {
    margin: 0;
    width: 1200px;
    height: 800px;
    overflow: hidden;
    background: var(--backdrop);
  }
  .canvas { position: relative; width: 1200px; height: 800px; }
  .label {
    position: absolute;
    left: 34px; top: 198px;
    width: 1139px; height: 406px;
    background: var(--label-black);
    color: var(--ink-white);
    box-shadow: 2px 3px 6px rgba(0,0,0,0.45);
    font-family: var(--font-body);
  }
  .label__band {
    position: absolute; left: 0; right: 0; bottom: 0;
    height: 10px; background: var(--accent-blue);
  }
  /* Supplement facts panel */
  .facts {
    position: absolute; left: 28px; top: 24px;
    width: 288px; height: 299px;
    border: 1.5px solid var(--ink-white);
    box-sizing: border-box;
    padding: 8px 9px 0 9px;
    overflow: hidden;
  }
  .facts__title {
    font-family: var(--font-display);
    font-weight: 600;
    color: var(--accent-blue);
    font-size: 21px;
    letter-spacing: 1.2px;
    white-space: nowrap;
    margin: 0;
    line-height: 26px;
  }
  .facts__serving {
    display: flex; justify-content: space-between;
    font-size: 10.5px; line-height: 14px; margin-top: 3px;
    padding-bottom: 3px;
    white-space: nowrap;
    border-bottom: 3px solid var(--ink-white);
  }
  .facts__amount-head {
    text-align: right; font-family: var(--font-display);
    font-weight: 500; font-size: 12px; line-height: 15px;
    padding: 6px 0 6px;
    border-bottom: 2px solid var(--ink-white);
  }
  .facts__row {
    display: flex; justify-content: space-between; align-items: center;
    box-sizing: border-box;
    height: 30px;
    border-bottom: 1.5px solid var(--ink-white);
    font-size: 14px; letter-spacing: 0.6px;
    padding: 0 1px 0 4px;
  }
  .facts__dose { font-family: var(--font-display); font-weight: 600; font-size: 13px; letter-spacing: 0; }
  .facts__note { font-size: 11px; line-height: 14px; letter-spacing: 0.5px; padding: 6px 4px 0; white-space: nowrap; }
  /* Company block */
  .company { position: absolute; left: 27px; top: 329px; }
  .company__name {
    font-family: var(--font-display); font-weight: 600;
    font-size: 18px; line-height: 22px; letter-spacing: 0.5px; margin: 0 0 4px;
  }
  .company__address { font-size: 14px; line-height: 18px; letter-spacing: 0.4px; margin: 0; }
  /* Centre brand block */
  .brand { position: absolute; left: 330px; width: 584px; top: 0; height: 100%; text-align: center; }
  .brand__mark {
    position: absolute; left: 50%; top: 52px; transform: translateX(-50%);
    display: flex; align-items: center; gap: 10px;
    font-family: var(--font-display); font-weight: 600;
    font-size: 22px; letter-spacing: 4px; white-space: nowrap;
  }
  .brand__mark-square { width: 22px; height: 22px; background: var(--ink-white); }
  .brand__name {
    position: absolute; left: 0; right: 0; top: 180px;
    font-family: var(--font-display); font-weight: 600;
    font-size: 42px; letter-spacing: 1px; margin: 0; line-height: 56px; white-space: nowrap;
  }
  .brand__tagline {
    position: absolute; left: 0; right: 0; top: 250px;
    font-size: 29px; letter-spacing: 1.5px; color: var(--accent-blue);
    line-height: 36px; white-space: nowrap;
  }
  .brand__tagline .sep { color: var(--ink-white); }
  .brand__underline {
    position: absolute; left: 128px; width: 398px; top: 287px;
    height: 3px; background: var(--accent-blue);
  }
  .brand__volume {
    position: absolute; left: 0; right: 0; top: 323px;
    font-family: var(--font-display); font-size: 32px; line-height: 40px;
  }
  .brand__volume b { font-weight: 700; }
  .brand__volume span { font-weight: 500; font-family: var(--font-body); }
  .brand__web { position: absolute; left: 0; right: 0; top: 371px; font-size: 13px; letter-spacing: 1px; }
  /* Certification badges */
  .badges { position: absolute; left: 960px; top: 0; width: 110px; height: 100%; }
  .badges svg { position: absolute; left: 0; top: 0; }
</style>
</head>
<body>
<div class="canvas">
  <section class="label">
    <div class="facts">
      <h2 class="facts__title">SUPPLEMENT FACTS</h2>
      <div class="facts__serving"><span>Serving Size: 1 Capsule</span><span>Serving Per Container:30</span></div>
      <div class="facts__amount-head">Amount Per Serving</div>
      <div class="facts__row"><span>Blueberry pterostilbene</span><span class="facts__dose">10mg</span></div>
      <div class="facts__row"><span>Bacopa</span><span class="facts__dose">150mg</span></div>
      <div class="facts__row"><span>Gingko Biloba</span><span class="facts__dose">50mg</span></div>
      <div class="facts__row"><span>Vinpocetine</span><span class="facts__dose">10mg</span></div>
      <div class="facts__row"><span>Alpha-GPC</span><span class="facts__dose">150mg</span></div>
      <div class="facts__row"><span>TAU</span><span class="facts__dose">35mg</span></div>
      <div class="facts__note">Daily Value (DV) not established.</div>
    </div>

    <div class="company">
      <p class="company__name">VELBROOK NUTRITION</p>
      <p class="company__address">48 Alder Row #310,<br>Harlow City-27-41-00</p>
    </div>

    <div class="brand">
      <div class="brand__mark"><span class="brand__mark-square"></span>VELBROOK</div>
      <h1 class="brand__name">VELBROOK NUTRITION</h1>
      <div class="brand__tagline">MEMORY<span class="sep">-</span>FOCUS<span class="sep">-</span>CLARITY</div>
      <div class="brand__underline"></div>
      <div class="brand__volume"><b>60</b><span>ml</span></div>
      <div class="brand__web">www.Velbrook.example</div>
    </div>

    <div class="badges">
      <svg width="140" height="406" viewBox="0 0 140 406" role="img" aria-label="Certification badges">
        <rect x="9" y="33" width="88" height="54" fill="none" stroke="#fff" stroke-width="3"/>
        <circle cx="53" cy="146" r="37" fill="none" stroke="#fff" stroke-width="3"/>
        <circle cx="53" cy="146" r="22" fill="#fff"/>
        <rect x="3" y="216" width="100" height="34" rx="4" fill="#fff"/>
        <rect x="10" y="253" width="86" height="3" fill="#e02020"/>
        <circle cx="53" cy="318" r="33" fill="none" stroke="#fff" stroke-width="3"/>
        <rect x="15" y="306" width="76" height="24" rx="6" fill="#fff"/>
      </svg>
    </div>

    <div class="label__band"></div>
  </section>
</div>
</body>
</html>
```